New business card for civil engineering company - "Keystone Audit"

We need a business card designed for our new structural engineering company.

The company name is "Keystone Audit" logo files attached.

We would like the following:
* Two-sided card
* Simple design

Information to be placed on the card:
Name - Marcus Dellow
Job Title - Director / Structural Engineer
Credentials - BEng(Hons), CPEng, CMengNZ, IntPE(NZ)
Email - marcus.dellow@keystoneaudit.co.nz
mobile - 0219364058
website - www.keystoneaudit.co.nz

```html
<!DOCTYPE html>
<html lang="en">
<head>
<meta charset="UTF-8">
<title>Keystone Audit — Business Card</title>
<link href="https://fonts.googleapis.com/css2?family=Open+Sans:wght@400;600;700&display=swap" rel="stylesheet">
<style>
  :root {
    --navy: #15416f;
    --accent: #6b8fcb;
    --white: #ffffff;
    --ink: #3a3d42;
    --backdrop: #d9dcdf;
  }
  * { margin: 0; padding: 0; box-sizing: border-box; }
  html, body { width: 1200px; height: 977px; overflow: hidden; }
  body {
    background: var(--backdrop);
    font-family: "Open Sans", sans-serif;
    position: relative;
  }
  .card {
    position: absolute;
    left: 220px;
    width: 760px;
    height: 434px;
    overflow: hidden;
    box-shadow: 0 6px 18px rgba(0,0,0,0.18);
  }
  .card--front { top: 36px; background: var(--navy); }
  .card--back { top: 507px; background: var(--white); }

  .brand {
    display: flex;
    align-items: center;
    gap: 14px;
    font-weight: 600;
    font-size: 40px;
    letter-spacing: 0.04em;
    white-space: nowrap;
  }
  .brand__mark { width: 26px; height: 26px; }
  .card--front .brand {
    position: absolute;
    left: 50%; top: 50%;
    transform: translate(-50%, -50%);
    color: var(--white);
  }
  .card--front .brand__mark { background: var(--white); }

  .back__panel {
    position: absolute;
    left: 0; top: 0;
    width: 362px; height: 100%;
    background: var(--navy);
    color: var(--white);
    padding: 118px 0 0 62px;
  }
  .person__name { font-size: 27px; font-weight: 700; line-height: 1.2; }
  .person__title { font-size: 16px; font-weight: 400; margin-top: 2px; }
  .person__credentials { font-size: 11.5px; font-weight: 600; margin-top: 2px; }
  .contact { list-style: none; margin-top: 44px; }
  .contact__item {
    display: flex; align-items: center; gap: 12px;
    font-size: 14px; margin-bottom: 9px;
  }
  .contact__icon { width: 13px; height: 13px; flex: none; }

  .back__sliver { position: absolute; left: 376px; top: 0; width: 40px; height: 100%; }
  .card--back .brand {
    position: absolute;
    left: 590px; top: 50%;
    transform: translate(-50%, -50%);
    color: var(--ink);
    font-size: 34px;
  }
  .card--back .brand__mark { background: var(--accent); width: 22px; height: 22px; }
</style>
</head>
<body>
  <section class="card card--front" aria-label="Card front">
    <div class="brand"><span class="brand__mark"></span>Keystone Audit</div>
  </section>

  <section class="card card--back" aria-label="Card back">
    <div class="back__panel">
      <h1 class="person__name">Marcus Dellow</h1>
      <p class="person__title">Director / Structural Engineer</p>
      <p class="person__credentials">BEng(Hons), CPEng, CMengNZ, IntPE(NZ)</p>
      <ul class="contact">
        <li class="contact__item">
          <svg class="contact__icon" viewBox="0 0 24 24" fill="#fff"><path d="M6.6 10.8a15 15 0 0 0 6.6 6.6l2.2-2.2a1 1 0 0 1 1-.25 11.4 11.4 0 0 0 3.6.6 1 1 0 0 1 1 1V20a1 1 0 0 1-1 1A17 17 0 0 1 3 4a1 1 0 0 1 1-1h3.5a1 1 0 0 1 1 1c0 1.25.2 2.45.6 3.6a1 1 0 0 1-.25 1z"/></svg>
          0219364058
        </li>
        <li class="contact__item">
          <svg class="contact__icon" viewBox="0 0 24 24" fill="#fff"><path d="M2 5h20v14H2z M2 5l10 8 10-8" stroke="#15416f" stroke-width="1.5"/></svg>
          marcus.dellow@keystoneaudit.co.nz
        </li>
        <li class="contact__item">
          <svg class="contact__icon" viewBox="0 0 24 24" fill="none" stroke="#fff" stroke-width="2"><circle cx="12" cy="12" r="10"/><path d="M2 12h20M12 2c3 3 3 17 0 20M12 2c-3 3-3 17 0 20"/></svg>
          www.keystoneaudit.co.nz
        </li>
      </ul>
    </div>
    <svg class="back__sliver" viewBox="0 0 40 434" preserveAspectRatio="none" aria-hidden="true">
      <polygon points="6,0 10,0 40,434 22,434" fill="var(--accent)"/>
    </svg>
    <div class="brand"><span class="brand__mark"></span>Keystone Audit</div>
  </section>
</body>
</html>
```